KTR Associates Business Card

I would like to have a business card designed that uses my current logo and colors. I am not looking for anything to "out there" but can have a little fun so that it stands out.

I have a boutique consulting firm that specializes in strategic planning, change management, leadership development and innovation.

Industry/Entity Type

Leadership

Contact Information for Business Card

Marta Holbeck
President
marta@ktr-associates.example
555-014-2286

```html
<!DOCTYPE html>
<html lang="en">
<head>
<meta charset="utf-8">
<title>KTR Associates Business Card</title>
<link rel="stylesheet" href="https://fonts.googleapis.com/css2?family=Cormorant+Garamond:wght@500&family=Open+Sans:wght@400&display=swap">
<style>
  :root {
    --backdrop: #e9e9e9;
    --card-white: #ffffff;
    --card-black: #111111;
    --card-black-edge: #050505;
    --brand-green: #3e7f36;
    --ink: #222222;
    --ink-soft: #444444;
    --rule: #9a9a9a;
  }
  * { box-sizing: border-box; margin: 0; padding: 0; }
  html, body {
    width: 1200px; height: 1200px; overflow: hidden;
    background: var(--backdrop);
  }
  .card-sheet {
    position: absolute; inset: 0;
    display: flex; align-items: center; justify-content: center; gap: 40px;
  }
  .card {
    position: relative;
    width: 500px; height: 290px;
    box-shadow: 0 4px 14px rgba(0,0,0,0.18);
    overflow: hidden;
  }
  .card--front { background: var(--card-white); }
  .card--back {
    background:
      radial-gradient(ellipse at 50% 40%, #2a2a2a 0%, var(--card-black) 55%, var(--card-black-edge) 100%);
  }
  .wordmark {
    position: absolute; left: 0; right: 0;
    text-align: center;
    font-family: "Cormorant Garamond", Georgia, serif;
    font-weight: 500;
    font-size: 40px;
    letter-spacing: 1px;
    line-height: 1;
  }
  .card--front .wordmark { top: 72px; color: var(--ink); }
  .card--back .wordmark { top: 122px; color: #ffffff; }

  .holder {
    position: absolute; left: 34px; top: 189px;
    font-family: "Open Sans", Arial, sans-serif;
  }
  .holder-name { font-size: 15px; color: var(--ink-soft); line-height: 1.2; }
  .holder-name .surname { color: var(--brand-green); }
  .holder-title { font-size: 10px; color: var(--ink-soft); margin-top: 2px; }

  .contact-rule {
    position: absolute; left: 34px; right: 10px; top: 238px;
    height: 1px; background: var(--rule);
  }
  .contact-row {
    position: absolute; left: 28px; top: 245px;
    display: flex; gap: 38px;
    font-family: "Open Sans", Arial, sans-serif;
    font-size: 11.5px; color: var(--brand-green); letter-spacing: 0.3px;
  }
  .contact-item { display: flex; align-items: center; gap: 6px; }
  .contact-item svg { width: 13px; height: 13px; display: block; }
  .contact-band {
    position: absolute; left: 0; right: 0; bottom: 0;
    height: 25px; background: var(--brand-green);
  }
</style>
</head>
<body>
  <main class="card-sheet">
    <section class="card card--front" aria-label="Card front">
      <div class="wordmark">KTR Associates</div>
      <div class="holder">
        <p class="holder-name">Marta <span class="surname">Holbeck</span></p>
        <p class="holder-title">President</p>
      </div>
      <div class="contact-rule"></div>
      <div class="contact-row">
        <span class="contact-item">
          <svg viewBox="0 0 14 14" aria-hidden="true">
            <rect width="14" height="14" rx="2" fill="#3e7f36"/>
            <path d="M4.2 3 L5.8 3 L6.4 5 L5.4 6 Q6.2 7.8 8 8.6 L9 7.6 L11 8.2 L11 9.8 Q10.6 11 9.3 11 Q3 10.4 3 4.7 Q3 3.4 4.2 3 Z" fill="#fff"/>
          </svg>
          555-014-2286
        </span>
        <span class="contact-item">
          <svg viewBox="0 0 14 14" aria-hidden="true">
            <rect width="14" height="14" rx="2" fill="#3e7f36"/>
            <circle cx="7" cy="7" r="3.8" fill="none" stroke="#fff" stroke-width="1.2"/>
            <circle cx="7" cy="7" r="1.4" fill="none" stroke="#fff" stroke-width="1.1"/>
          </svg>
          marta@ktr-associates.example
        </span>
      </div>
      <div class="contact-band"></div>
    </section>

    <section class="card card--back" aria-label="Card back">
      <div class="wordmark">KTR Associates</div>
    </section>
  </main>
</body>
</html>
```